Mortgage Broking boutique Business

I’m wanting a revamped look to my existing business card design. I do like the black and silver but happy to have other colours introduced based on your creation. I’ve attached a copy of my current card so you can have a starting point updated details noted brloe. I deal with high net worth individuals so need my card to be sophisticated, classy that gives off a classy vibe

Target Market(s)

High net worth, wealthy

Industry/Entity Type

Mortgage Brokerage

Contact Information for Business Card

Job title: Finance Executive
Phone: +61 7 3287 4419
Mobile: 0471 352 608
Email: marcus@quillbrookcapital.com.au
Web: www.quillbrookcapital.com.au
Address: level 36 Tindale Court, 58 Harwick St Brisbane QLD 4000

Font styles to use
Other font styles liked:
• Helvetica

Colors

Designer to choose colors to be used in the design.

Requirements
Must have
• Use my existing card design as a starting point

```html
<!DOCTYPE html>
<html lang="en">
<head>
<meta charset="utf-8">
<title>Quillbrook Capital – Business Card</title>
<link href="https://fonts.googleapis.com/css2?family=Arimo:wght@400;700&display=swap" rel="stylesheet">
<style>
  :root {
    --backdrop: #2a2d31;
    --card: #0d0d0e;
    --silver: #d9d9d9;
    --silver-soft: #b9b9b9;
    --white: #f4f4f4;
  }
  * { box-sizing: border-box; margin: 0; padding: 0; }
  html, body {
    width: 1200px;
    height: 900px;
    overflow: hidden;
    background: var(--backdrop);
    font-family: "Arimo", Helvetica, Arial, sans-serif;
  }
  .stage {
    position: relative;
    width: 1200px;
    height: 900px;
  }
  .card {
    position: absolute;
    top: 297px;
    width: 500px;
    height: 305px;
    background: var(--card);
    border-radius: 22px;
  }
  .card--contact { left: 70px; }
  .card--brand { left: 630px; }

  /* Frames */
  .frame {
    position: absolute;
    inset: 24px;
    border: 2px solid var(--silver);
  }
  .frame--double { inset: 20px; }
  .frame--double::after {
    content: "";
    position: absolute;
    inset: 5px;
    border: 2px solid var(--silver);
  }

  /* Brand side */
  .brand-name {
    position: absolute;
    inset: 0;
    display: flex;
    flex-direction: column;
    align-items: center;
    justify-content: center;
    gap: 6px;
    color: var(--silver);
    font-weight: 700;
    white-space: nowrap;
  }
  .brand-name__main {
    font-size: 28px;
    letter-spacing: 0.3em;
    margin-right: -0.3em;
  }
  .brand-name__sub {
    font-size: 15px;
    letter-spacing: 0.2em;
    margin-right: -0.2em;
  }

  /* Contact side */
  .contact {
    position: absolute;
    inset: 24px;
    padding: 30px 18px 0 28px;
    color: var(--white);
  }
  .contact__brand {
    display: flex;
    align-items: center;
    gap: 10px;
    font-weight: 700;
    font-size: 18px;
    letter-spacing: 0.2em;
    color: var(--silver);
    white-space: nowrap;
  }
  .contact__brand-mark {
    width: 10px;
    height: 10px;
    background: var(--silver);
  }
  .contact__name {
    margin-top: 18px;
    font-weight: 700;
    font-size: 21px;
    letter-spacing: 0.02em;
  }
  .contact__title {
    margin-top: 2px;
    font-size: 14px;
    color: var(--silver-soft);
  }
  .contact__details {
    margin-top: 26px;
    font-size: 11.5px;
    line-height: 1.8;
    color: var(--silver-soft);
  }
  .contact__row { white-space: nowrap; }
  .contact__row span + span { margin-left: 16px; }
</style>
</head>
<body>
<main class="stage">
  <section class="card card--contact" aria-label="Contact side of business card">
    <div class="frame"></div>
    <div class="contact">
      <div class="contact__brand"><span class="contact__brand-mark"></span>QUILLBROOK.CAPITAL</div>
      <h1 class="contact__name">MARCUS BELLAMY</h1>
      <p class="contact__title">Finance Executive</p>
      <div class="contact__details">
        <p class="contact__row"><span>M: 0471 352 608</span><span>P: +61 7 3287 4419</span></p>
        <p class="contact__row"><span>W: www.quillbrookcapital.com.au</span><span>E: marcus@quillbrookcapital.com.au</span></p>
        <p class="contact__row">level 36 Tindale Court, 58 Harwick St Brisbane QLD 4000</p>
      </div>
    </div>
  </section>

  <section class="card card--brand" aria-label="Brand side of business card">
    <div class="frame frame--double"></div>
    <p class="brand-name">
      <span class="brand-name__main">QUILLBROOK</span>
      <span class="brand-name__sub">CAPITAL</span>
    </p>
  </section>
</main>
</body>
</html>
```